I need a label design to go on our jars of honey. Our company is called Marlowe Honey Co. The type of honey is called Ridgefern Gold Honey. The jars are 1kg. Attached is the label size. Left hand side needs to have nutritional info... as attached. Middle section is our company name, honey type, 1kg & Whangamata, NZ. Right hand side needs to have info as per photo (raw honey etc). I would like to upload more pictures... but I’m unsure how to do this? Thanks, Carol

Target Market(s)

Honey consumers... families

Industry/Entity Type

Food Production

Colors

Designer to choose colors to be used in the design.

Requirements
Must have
• Nutritional info as per upload
• Type of honey & company name as per upload
• 1kg
• Address
Nice to have
• Similar fonts to upload.
• Possibly background image... floral or beach... very faint though.

```html
<!DOCTYPE html>
<html lang="en">
<head>
<meta charset="utf-8">
<title>Marlowe Honey Co. – Ridgefern Gold Honey Label</title>
<link rel="stylesheet" href="https://fonts.googleapis.com/css2?family=Bitter:ital,wght@0,400;0,600;0,700;1,400;1,700&family=Delius&family=Lobster+Two:wght@700&display=swap">
<style>
  :root {
    --page: #ebe7de;
    --honey: #e8b143;
    --paper: #ffffff;
    --ink: #3b2b14;
    --cream: #fff6e2;
    --rule: rgba(255, 246, 226, 0.55);
    --bee-dark: #2b2116;
    --bee-gold: #f2b51c;
  }
  * { box-sizing: border-box; margin: 0; padding: 0; }
  html, body {
    width: 1200px; height: 600px; overflow: hidden;
    background: var(--page);
  }
  .canvas { position: relative; width: 1200px; height: 600px; }

  .label {
    position: absolute; left: 40px; top: 76px;
    width: 1120px; height: 448px;
    background: var(--honey);
    box-shadow: 0 4px 14px rgba(0,0,0,0.18);
    font-family: "Bitter", serif;
    color: var(--ink);
  }
  .label__top, .label__bottom {
    position: absolute; left: 0; right: 0; background: var(--paper);
  }
  .label__top { top: 0; height: 34px; }
  .label__bottom {
    bottom: 0; height: 38px;
    display: flex; align-items: center;
    font-size: 13px; color: var(--honey);
  }
  .label__bottom span { position: absolute; transform: translateX(-50%); white-space: nowrap; }

  .bee {
    position: absolute; top: 10px; width: 34px; height: 42px;
    transform: translateX(-50%);
    border-radius: 50% 50% 45% 45%;
    background: linear-gradient(180deg, var(--bee-gold) 0%, var(--bee-dark) 60%, var(--bee-gold) 100%);
  }

  /* Nutrition panel */
  .nutrition { position: absolute; left: 32px; top: 72px; width: 256px; }
  .nutrition__title {
    text-align: center; font-weight: 700; font-size: 16.5px; color: var(--cream);
    margin-bottom: 12px;
  }
  .nutrition__row {
    display: grid; grid-template-columns: 1fr 72px 62px;
    font-size: 13.5px; height: 22.6px; line-height: 22.6px;
    border-bottom: 1px dashed var(--rule);
    white-space: nowrap;
  }
  .nutrition__row span:nth-child(n+2) { text-align: right; }
  .nutrition__row--wide { grid-template-columns: 1fr 62px; }
  .nutrition__row--head {
    font-size: 9.5px; font-weight: 700; text-transform: uppercase; color: var(--cream);
    margin-top: 8px;
  }
  .nutrition__row--sub span:first-child { padding-left: 12px; }
  .nutrition__row:last-of-type { border-bottom: none; }
  .batch-box {
    margin-top: 14px; background: var(--paper); border-radius: 2px;
    height: 45px; padding: 4px 8px;
    font-size: 9.5px; font-weight: 700;
    display: grid; grid-template-columns: 105px 1fr; grid-template-rows: 1fr 1fr;
    align-items: center;
  }
  .batch-box span:first-child { grid-column: 1 / 3; border-bottom: 1px solid #eee; }

  /* Front panel */
  .front {
    position: absolute; left: 420px; width: 280px; top: 0; height: 410px;
    text-align: center;
  }
  .front__company {
    position: absolute; top: 80px; width: 100%;
    font-family: "Delius", cursive; font-size: 25px;
  }
  .front__rule {
    position: absolute; left: 68px; width: 144px; height: 2px; background: var(--cream);
  }
  .front__title {
    position: absolute; top: 158px; width: 100%;
    font-family: "Lobster Two", cursive; font-weight: 700;
    font-size: 60px; line-height: 56px; color: var(--paper);
    white-space: nowrap;
    text-shadow: 0 2px 2px rgba(120, 70, 0, 0.25);
  }
  .front__title span { display: block; }
  .front__weight { position: absolute; top: 333px; width: 100%; font-size: 19px; color: var(--cream); }
  .front__origin { position: absolute; top: 374px; width: 100%; font-size: 14px; }

  /* Story panel */
  .story {
    position: absolute; left: 828px; top: 70px; width: 264px;
    text-align: center; font-size: 13px; line-height: 16.5px;
  }
  .story__block { padding: 7px 0; border-bottom: 1px dashed var(--rule); }
  .story__block:last-child { border-bottom: none; }
  .story__kicker { font-size: 9.5px; font-weight: 700; text-transform: uppercase; color: var(--cream); line-height: 12px; }
  .story__source { font-size: 14px; color: var(--cream); }
  .story__block--first { padding-top: 0; }
  .story__praise { font-style: italic; }
  .story__praise b { font-weight: 700; }
  .dot { color: var(--cream); }
</style>
</head>
<body>
<div class="canvas">
  <section class="label" aria-label="Ridgefern Gold Honey jar label">
    <div class="label__top"></div>
    <div class="bee" style="left:160px" role="img" aria-label="Bee illustration"></div>
    <div class="bee" style="left:560px" role="img" aria-label="Bee illustration"></div>
    <div class="bee" style="left:960px" role="img" aria-label="Bee illustration"></div>

    <div class="nutrition">
      <h2 class="nutrition__title">Nutritional Information</h2>
      <div class="nutrition__row nutrition__row--wide"><span>Serving per package</span><span>100</span></div>
      <div class="nutrition__row nutrition__row--wide"><span>Serving size</span><span>10g</span></div>
      <div class="nutrition__row nutrition__row--head"><span>Average quantity</span><span>Per serving</span><span>Per 100g</span></div>
      <div class="nutrition__row"><span>Energy</span><span>134kj</span><span>1340kj</span></div>
      <div class="nutrition__row"><span>Protein</span><span>0.04g</span><span>0.4g</span></div>
      <div class="nutrition__row"><span>Fat total</span><span>0g</span><span>0g</span></div>
      <div class="nutrition__row nutrition__row--sub"><span>– saturated</span><span>0g</span><span>0g</span></div>
      <div class="nutrition__row"><span>Carbonhydrate</span><span>7.9g</span><span>79.6g</span></div>
      <div class="nutrition__row nutrition__row--sub"><span>– sugars</span><span>7.8g</span><span>78.1g</span></div>
      <div class="nutrition__row"><span>Sodium</span><span>1.2mg</span><span>12mg</span></div>
      <div class="batch-box"><span>BEST BEFORE :</span><span>RMP :</span><span>BATCH NO :</span></div>
    </div>

    <div class="front">
      <p class="front__company">Marlowe Honey Co.</p>
      <div class="front__rule" style="top:138px"></div>
      <h1 class="front__title"><span>Ridgefern</span><span>Gold Honey</span></h1>
      <div class="front__rule" style="top:302px"></div>
      <p class="front__weight">1 kg</p>
      <p class="front__origin">Whangamata, NZ</p>
    </div>

    <div class="story">
      <div class="story__block story__block--first">
        <p class="story__kicker">Sourced from</p>
        <p class="story__source">the beautiful Coromandel Peninsula</p>
      </div>
      <div class="story__block">Our honey comes to you raw &amp; unpasteurised, ensuring it retains all the natural goodness!</div>
      <div class="story__block">Arohanui,<br>Graham, Carol &amp; Boys</div>
      <div class="story__block story__praise"><b>Marlowe</b> - all thanks to God for His incredible creation!</div>
      <div class="story__block">Store upright in a cool, dry place. <span class="dot">•</span> No refrigeration needed. <span class="dot">•</span> Not recommend&shy;ed for infants below the age of 12 months.</div>
      <div class="story__block">24 Kereru Lane<br>Whangamata, New Zealand</div>
    </div>

    <div class="label__bottom">
      <span style="left:160px">No added ingredients</span>
      <span style="left:560px">100% New Zealand Honey</span>
      <span style="left:960px">www.marlowehoney.co.nz</span>
    </div>
  </section>
</div>
</body>
</html>
```